Ranked amongst the Best Colleges and Programs

the size of the ad is Full Page, with bleed*
8”x 10.75" plus 0.25" bleed'
you have two choices for the tagline .. please chose what ever you think will allow you to make a better ad.
The instructions on the brief are in red
I am looking for a hight quality modern ad to place in local weekly publications that will stand out .
I would like a ad that people will look at and say i would like to see what this ad is all about.
I apprecate creative work.
the ad should not be very crowded and the text should be able to be read.
if you decide to use people in the ad .. (you don't have to ) then it should be a male dressed in white shirt in and sports jacket.. or if you would like you can use a vector and then use male or female people.
please leave one inch on the bottom for the footer

Target Market(s)

potential middle class students from 23-35 years of age

Industry/Entity Type

education

Requirements
Must have
• .the " 98% employment rate" should stand out in the ad.. but should not be the main part of the ad
Nice to have
• creative
Should not have
• Should not be a very busy or crowded ad.. i prefer pictures of men but should be .. in a business suit .. that looks professional- white shirt

```html
<!DOCTYPE html>
<html lang="en">
<head>
<meta charset="utf-8">
<title>NHU Masters of Accounting – Full Page Ad</title>
<link rel="stylesheet" href="https://fonts.googleapis.com/css2?family=Bebas+Neue&family=Roboto+Condensed:wght@300;400&display=swap">
<style>
  :root {
    --page-bg: #ececec;
    --navy: #26235c;
    --band: #2b2d80;
    --cyan: #29a9e0;
    --yellow: #f2e51b;
    --white: #ffffff;
    --footer: #f7f7f7;
  }
  html, body {
    margin: 0;
    width: 1200px;
    height: 1200px;
    overflow: hidden;
    background: var(--page-bg);
  }
  .ad {
    position: absolute;
    left: 166px;
    top: 17px;
    width: 868px;
    height: 1165px;
  }
  .display { font-family: "Bebas Neue", "Oswald", sans-serif; }
  .body-copy { font-family: "Roboto Condensed", "Arial Narrow", sans-serif; }
  .headline-lead { fill: var(--cyan); font-size: 93px; }
  .headline-main { fill: var(--yellow); font-size: 116px; }
  .program-name { fill: var(--yellow); font-size: 38px; }
  .rank-label { fill: var(--cyan); font-size: 40px; }
  .rank-item { fill: var(--white); font-size: 31px; font-weight: 300; }
  .rank-source { fill: var(--yellow); }
  .stat-figure { fill: var(--white); font-size: 158px; }
  .stat-label { fill: var(--white); font-size: 54px; }
  .stat-note { fill: var(--cyan); font-size: 19px; font-weight: 400; }
  .rule { stroke: var(--yellow); stroke-width: 1.5; }
  .rank-frame { stroke: var(--white); stroke-width: 2.5; fill: none; }
</style>
</head>
<body>
<svg class="ad" viewBox="0 0 868 1165" xmlns="http://www.w3.org/2000/svg">
  <!-- base panels -->
  <rect class="panel" x="0" y="0" width="868" height="1046" fill="var(--navy)"/>
  <rect class="footer-space" x="0" y="1046" width="868" height="119" fill="var(--footer)"/>

  <!-- diagonal accent band -->
  <polygon class="accent-band" points="0,602 868,113 868,437 0,926" fill="var(--band)"/>
  <polygon class="accent-band-top" points="600,245 852,15 852,113 600,245" fill="var(--band)"/>
  <polyline class="accent-bracket" points="600,245 833,113 833,165 812,178 812,220" fill="none" stroke="var(--navy)" stroke-width="12"/>
  <polyline class="accent-bracket" points="16,1018 266,874 266,860" fill="none" stroke="var(--band)" stroke-width="14"/>
  <polyline class="accent-bracket" points="0,920 40,896 40,870" fill="none" stroke="var(--band)" stroke-width="14"/>

  <!-- headline -->
  <text class="display headline-lead" x="434" y="138" text-anchor="middle">A SMALL</text>
  <text class="display headline-lead" x="434" y="229" text-anchor="middle">INVESTMENT TODAY</text>
  <text class="display headline-main" x="434" y="348" text-anchor="middle">A BIG DIFFERENCE</text>
  <text class="display headline-main" x="434" y="456" text-anchor="middle">TOMORROW</text>

  <!-- program name -->
  <line class="rule" x1="203" y1="487" x2="665" y2="487"/>
  <text class="display program-name" x="434" y="524" text-anchor="middle">NHU- MASTERS OF ACCOUNTING</text>
  <line class="rule" x1="203" y1="534" x2="665" y2="534"/>

  <!-- rankings -->
  <text class="display rank-label" x="78" y="619">RANKED AMONGST</text>
  <polyline class="rank-frame" points="340,608 797,608 797,754 86,754 86,634"/>
  <text class="body-copy rank-item" x="124" y="667">BEST COLLEGES-<tspan class="rank-source">CAPITAL REVIEW 2023</tspan></text>
  <text class="body-copy rank-item" x="124" y="721">BEST MASTERS IN ACCOUNTING - <tspan class="rank-source">GRADRANK 2023</tspan></text>

  <!-- employment stat -->
  <text class="display stat-figure" x="82" y="910">98%</text>
  <text class="display stat-label" x="324" y="912">EMPLOYMENT RATE</text>
  <text class="body-copy stat-note" x="434" y="972" text-anchor="middle">NHU graduates have gone on to work in various high-quality jobs in top firms,</text>
  <text class="body-copy stat-note" x="434" y="1003" text-anchor="middle">earning impressive six-figure salaries as well as opening successful businesses.</text>
</svg>
</body>
</html>
```